We have an approved label for 20L kegs that match with the company name. Now we need to make another label (5 x 3.5 in) more attractive to be used in bottles. We are going to bottling (750ML) wine from kegs. We want to keep, if possible, a relation between both labels, such as the color, appeal to the concept of freshness, directly from the vineyard to your glass, eco-friendly, elegant/ artistic, new way of drinking, the solution or path to the future. We drafted a label with our vision so you can be inspired and complete our idea. Brand is Vuelo Claro (clear flight), varietal and vintage as well as volume are changeable. Company logo is also included for your reference and we would like to be included in the back label or part of it, and also the phrase Rook Wine is another element that we used for our marketing. Any further information contact us.

```html
<!DOCTYPE html>
<html lang="en">
<head>
<meta charset="UTF-8">
<title>Vuelo Claro – 2017 Chardonnay Labels</title>
<link rel="stylesheet" href="https://fonts.googleapis.com/css2?family=Allura&family=Cormorant+Garamond:wght@600&family=Montserrat:wght@900&family=Roboto:wght@400&family=Roboto+Condensed:wght@400;700&display=swap">
<style>
  :root {
    --page-bg: #ededed;
    --label-bg: #ffffff;
    --ink: #111111;
    --ink-soft: #222222;
    --art-light: #c4c4c4;
    --art-dark: #4a4a4a;
    --badge: #e8a33a;
  }
  * { margin: 0; padding: 0; box-sizing: border-box; }
  html, body {
    width: 1200px; height: 814px; overflow: hidden;
    background: var(--page-bg);
  }
  .canvas { position: relative; width: 1200px; height: 814px; }

  .label {
    position: absolute;
    background: var(--label-bg);
    color: var(--ink);
    overflow: hidden;
  }

  /* Front label */
  .front-label { left: 118px; top: 123px; width: 430px; height: 582px; }
  .front-label .vintage-title {
    position: absolute; top: 44px; left: 0; width: 100%;
    text-align: center;
    font-family: "Cormorant Garamond", serif;
    font-weight: 600; font-size: 31px;
    font-variant: small-caps; letter-spacing: 0.5px;
  }
  .pour-art { position: absolute; left: 0; top: 146px; width: 272px; height: 436px; }
  .brand-name {
    position: absolute; right: 26px; top: 176px;
    text-align: right;
    font-family: "Montserrat", sans-serif;
    font-weight: 900; font-size: 76px; line-height: 0.96;
    letter-spacing: -2px;
  }
  .tagline-mark {
    position: absolute; right: 28px; top: 372px;
    font-family: "Allura", cursive;
    font-size: 56px; line-height: 1;
  }
  .return-note {
    position: absolute; right: 32px; top: 502px;
    text-align: right;
    font-family: "Roboto", sans-serif;
    font-size: 15.5px; line-height: 17.5px;
  }

  /* Back label */
  .back-label { left: 614px; top: 227px; width: 431px; height: 375px; }
  .back-label .vintage-title {
    position: absolute; top: 18px; left: 0; width: 100%;
    text-align: center;
    font-family: "Cormorant Garamond", serif;
    font-weight: 600; font-size: 24px;
    font-variant: small-caps; letter-spacing: 0.3px;
  }
  .origin-line {
    position: absolute; top: 50px; left: 0; width: 100%;
    text-align: center;
    font-family: "Roboto", sans-serif; font-size: 13px;
  }
  .tasting-notes {
    position: absolute; top: 73px; left: 0; width: 100%;
    text-align: center; white-space: nowrap;
    font-family: "Roboto", sans-serif;
    font-size: 10.5px; line-height: 14px; color: var(--ink-soft);
  }
  .tasting-notes span, .gov-warning span { display: block; }
  .packer {
    position: absolute; top: 207px; left: 112px; width: 200px;
    text-align: center;
    font-family: "Roboto", sans-serif;
    font-size: 11px; line-height: 13px;
  }
  .partner-badge {
    position: absolute; left: 338px; top: 200px;
    width: 33px; height: 33px; border-radius: 50%;
    background: var(--badge);
  }
  .spec-row {
    position: absolute; left: 32px; right: 32px; top: 244px;
    display: flex; justify-content: space-between; align-items: center;
    font-family: "Roboto Condensed", sans-serif; font-weight: 700;
    font-size: 12.5px;
  }
  .gov-warning {
    position: absolute; top: 267px; left: 31px; right: 31px;
    font-family: "Roboto Condensed", sans-serif;
    font-size: 9.4px; line-height: 11.7px;
    text-transform: uppercase;
  }
  .gov-warning .justified { text-align: justify; text-align-last: justify; }
  .gov-warning strong { font-weight: 700; }
  .footer-item {
    position: absolute; top: 330px;
    display: flex; align-items: center; gap: 5px; height: 20px;
    font-family: "Roboto Condensed", sans-serif; font-weight: 700;
    font-size: 12.5px;
  }
  .footer-eco { left: 31px; }
  .footer-social-a { left: 129px; }
  .footer-social-b { left: 229px; }
  .footer-vegan { right: 32px; }
  .social-square { width: 19px; height: 19px; background: var(--ink); border-radius: 3px; }
</style>
</head>
<body>
<div class="canvas">

  <section class="label front-label">
    <h1 class="vintage-title">2017 Chardonnay</h1>
    <svg class="pour-art" viewBox="0 0 272 436" role="img" aria-label="Illustration area: a draft tap pouring a flowing striped ribbon of wine down the label">
      <defs>
        <linearGradient id="pourTone" x1="0" y1="0" x2="0" y2="1">
          <stop offset="0" stop-color="var(--art-light)"/>
          <stop offset="1" stop-color="var(--art-dark)"/>
        </linearGradient>
      </defs>
      <path d="M0 0 H110 V210 H222 V326 H272 V436 H0 Z" fill="url(#pourTone)"/>
    </svg>
    <div class="brand-name">VUELO<br>CLARO</div>
    <div class="tagline-mark">Rook Wine</div>
    <p class="return-note">Return the bottle<br>and get 25¢ in<br>next order</p>
  </section>

  <section class="label back-label">
    <h2 class="vintage-title">2017 Chardonnay</h2>
    <p class="origin-line">Light French Oak – Yakima Valley, WA</p>
    <p class="tasting-notes">
      <span>Aromas of honeysuckle, melon, flowers, toasted cashews… Ripe pears</span>
      <span>and lemons, crispy fresh acidity expressed in mouth… Elegant subtle</span>
      <span>creaminess finish with a touch of exotic oak spices… Fermented in</span>
      <span>stainless-steel followed by a partial malolactic fermentation in French</span>
      <span>oak barrels, rendering a nicely balanced Chardonnay with great structure,</span>
      <span>bright and abundant in fruit aromas. Ideal for pairing with poultry (chicken,</span>
      <span>guinea…), fish (salmon, codfish…) in lightly spiced buttery sauces,</span>
      <span>creamy pasta dishes, fresh veggie salads and soft-to-mild cheeses.</span>
      <span>Cheers!</span>
    </p>
    <p class="packer">Packed by &nbsp;&nbsp;&nbsp;&nbsp;&nbsp;&nbsp;&nbsp;&nbsp;&nbsp;&nbsp;&nbsp;&nbsp;&nbsp;&nbsp;&nbsp;&nbsp;&nbsp;&nbsp;&nbsp;&nbsp;&nbsp;. PR<br>and distributed by RIVP, Carolina, PR</p>
    <div class="partner-badge" aria-hidden="true"></div>
    <div class="spec-row"><span>CONTAIN SULFITES</span><span>750ML</span><span>ALC. 13.5% by VOL</span></div>
    <p class="gov-warning">
      <span class="justified"><strong>Government warning:</strong> (1) According to the Surgeon General, women</span>
      <span class="justified">should not drink alcoholic beverages during pregnancy because of</span>
      <span class="justified">the risk of birth defects. (2) Consumption of alcoholic beverages</span>
      <span class="justified">impairs your availability to drive a car or operate machinery, and may</span>
      <span>cause health problems.</span>
    </p>
    <div class="footer-item footer-eco">ECO-FRIENDLY</div>
    <div class="footer-item footer-social-a"><span class="social-square"></span>@RIVPPR</div>
    <div class="footer-item footer-social-b"><span class="social-square"></span>@rookwine</div>
    <div class="footer-item footer-vegan">VEGAN</div>
  </section>

</div>
</body>
</html>
```